Business Card for Makeup Artist

I need a business card designed for my makeup and hair artistry business which is primarily events and weddings focused. The card needs to be sleek, simple, stylish and appealing to women. I would prefer a white background but open to suggestions also. I also love the marble background look. I have attached some example pics. It needs to be a double sided card with logo and/or design on one side and contact details in the centre of the card on the other side. NO LOGO ON BACK. Examples attached.

Target Market(s)

Females age 14-55

Industry/Entity Type

Business

Contact Information for Business Card

Nora Vint
Principal Makeup Artist
P: 0413 925 214
E: nora@lumirabeauty.com.au
W: www.lumirabeauty.com.au

Requirements
Should not have
• No yellow, green, red or blue in the design.

```html
<!DOCTYPE html>
<html lang="en">
<head>
<meta charset="utf-8">
<title>Lumira Makeup Artistry – Business Card</title>
<link href="https://fonts.googleapis.com/css2?family=Lato:wght@400;700&display=swap" rel="stylesheet">
<style>
  :root {
    --stage: #d9d7d5;
    --card: #ebebeb;
    --ink: #555555;
    --ink-dark: #2e2e2e;
    --rule: #3a3a3a;
    --pill-text: #ffffff;
  }
  * { margin: 0; padding: 0; box-sizing: border-box; }
  html, body {
    width: 1200px; height: 799px; overflow: hidden;
    background: var(--stage);
    font-family: "Lato", Arial, sans-serif;
  }
  .stage {
    position: relative; width: 1200px; height: 799px;
    display: flex; align-items: center; justify-content: center; gap: 40px;
  }
  .card {
    position: relative; width: 520px; height: 297px;
    background: var(--card);
    box-shadow: 0 6px 18px rgba(0,0,0,0.18);
  }
  /* Front */
  .frame-line { position: absolute; background: var(--rule); }
  .frame-top    { top: 22px; left: 130px; width: 260px; height: 2px; }
  .frame-bottom { bottom: 22px; left: 180px; width: 220px; height: 2px; }
  .frame-left   { top: 60px; left: 34px; width: 2px; height: 170px; }
  .frame-right  { top: 40px; right: 34px; width: 2px; height: 170px; }
  .wordmark {
    position: absolute; inset: 0;
    display: flex; flex-direction: column; align-items: center; justify-content: center;
    color: var(--ink); font-weight: 400; text-align: center;
  }
  .wordmark-name { font-size: 72px; letter-spacing: 2px; line-height: 1; }
  .wordmark-line { font-size: 26px; letter-spacing: 1px; margin-top: 6px; }

  /* Back */
  .contact-head {
    position: absolute; top: 38px; left: 0; right: 0;
    display: flex; flex-direction: column; align-items: center;
  }
  .contact-name {
    font-size: 20px; font-weight: 700; letter-spacing: 1px;
    color: var(--ink-dark); text-transform: uppercase;
  }
  .contact-role {
    margin-top: 3px; padding: 2px 14px; border-radius: 10px;
    background: var(--ink-dark); color: var(--pill-text);
    font-size: 11px; font-weight: 700; letter-spacing: 0.5px; text-transform: uppercase;
  }
  .head-rule { margin-top: 22px; width: 56px; height: 2px; background: var(--rule); }
  .center-rule {
    position: absolute; left: 50%; top: 150px; width: 2px; height: 36px;
    background: var(--rule); transform: translateX(-50%);
  }
  .contact-col {
    position: absolute; display: flex; flex-direction: column; align-items: center;
    color: var(--ink-dark); font-size: 13px; letter-spacing: 0.5px; line-height: 1.35;
  }
  .col-web   { left: 40px; width: 210px; top: 180px; }
  .col-phone { right: 30px; width: 180px; top: 125px; }
  .contact-icon { width: 22px; height: 22px; margin-bottom: 14px; }
  .col-web .contact-icon { margin-bottom: 24px; }
</style>
</head>
<body>
<main class="stage">
  <section class="card card-front" aria-label="Card front">
    <span class="frame-line frame-top"></span>
    <span class="frame-line frame-left"></span>
    <span class="frame-line frame-right"></span>
    <span class="frame-line frame-bottom"></span>
    <div class="wordmark">
      <span class="wordmark-name">Lumira</span>
      <span class="wordmark-line">MAKEUP ARTISTRY</span>
    </div>
  </section>

  <section class="card card-back" aria-label="Card back">
    <div class="contact-head">
      <span class="contact-name">Nora Vint</span>
      <span class="contact-role">Principal Makeup Artist</span>
      <span class="head-rule"></span>
    </div>
    <span class="center-rule"></span>

    <div class="contact-col col-web">
      <svg class="contact-icon" viewBox="0 0 24 24" aria-hidden="true">
        <g fill="none" stroke="#2e2e2e" stroke-width="2.6" stroke-linecap="round">
          <rect x="3" y="10" width="10" height="6" rx="3" transform="rotate(-45 8 13)"/>
          <rect x="11" y="8" width="10" height="6" rx="3" transform="rotate(-45 16 11)"/>
        </g>
      </svg>
      <span>nora@lumirabeauty.com.au</span>
      <span>www.lumirabeauty.com.au</span>
    </div>

    <div class="contact-col col-phone">
      <svg class="contact-icon" viewBox="0 0 24 24" aria-hidden="true">
        <rect x="6" y="2" width="12" height="20" rx="2" fill="none" stroke="#2e2e2e" stroke-width="1.8"/>
        <line x1="10" y1="19" x2="14" y2="19" stroke="#2e2e2e" stroke-width="1.6"/>
      </svg>
      <span>0413 925 214</span>
    </div>
  </section>
</main>
</body>
</html>
```